BRL business card

For a business card with our logo

Contact Information for Business Card

Mathéo VRANEL
Founder & CEO
email : ceo@brightlanterncollective.com / www.brightlanterncollective.com /
instagram / facebook / WhatsApp
N°: +590 690 482 517

Colors

Designer to choose colors to be used in the design.

```html
<!DOCTYPE html>
<html lang="en">
<head>
<meta charset="UTF-8">
<title>BRL Business Card</title>
<link href="https://fonts.googleapis.com/css2?family=Roboto:wght@400;700&display=swap" rel="stylesheet">
<style>
  :root {
    --brand-blue: #1157a6;
    --brand-orange: #f07526;
    --card-white: #ffffff;
    --stage: #3a3d44;
  }
  * { margin: 0; padding: 0; box-sizing: border-box; }
  html, body { width: 1200px; height: 1000px; overflow: hidden; background: var(--stage); }
  body { font-family: "Roboto", Arial, sans-serif; position: relative; }

  .card {
    position: absolute;
    left: 210px;
    width: 780px;
    height: 446px;
    overflow: hidden;
    box-shadow: 0 14px 30px rgba(0,0,0,0.45);
  }
  .card--front { top: 44px; }
  .card--back { top: 516px; }
  .card__art { position: absolute; inset: 0; width: 100%; height: 100%; }

  .brand {
    position: absolute;
    display: flex;
    align-items: center;
    gap: 16px;
  }
  .brand__dot {
    width: 60px; height: 60px;
    border-radius: 50%;
    background: var(--brand-orange);
    flex: none;
  }
  .brand__name {
    color: var(--brand-blue);
    font-weight: 700;
    font-size: 25px;
    line-height: 1.15;
    letter-spacing: 1px;
  }
  .card--front .brand { left: 110px; top: 135px; }
  .card--back .brand { left: 470px; top: 200px; }

  .person { position: absolute; left: 62px; top: 92px; }
  .person__name {
    color: var(--brand-orange);
    font-weight: 700;
    font-size: 27px;
    letter-spacing: 0.5px;
  }
  .person__role {
    color: var(--card-white);
    font-size: 18px;
    margin-top: 6px;
  }

  .contacts { position: absolute; left: 62px; top: 262px; list-style: none; }
  .contacts__item {
    display: flex;
    align-items: center;
    gap: 12px;
    color: var(--card-white);
    font-size: 16px;
    height: 30px;
  }
  .contacts__icon { width: 18px; height: 18px; flex: none; }
  .contacts__social { display: flex; gap: 4px; flex: none; }
  .contacts__social span {
    width: 14px; height: 14px; border-radius: 50%;
    background: var(--brand-orange); display: block;
  }
</style>
</head>
<body>

  <section class="card card--front" aria-label="Card front">
    <svg class="card__art" viewBox="0 0 780 446" preserveAspectRatio="none" aria-hidden="true">
      <rect width="780" height="446" fill="var(--card-white)"/>
      <path d="M456 0 L780 0 L780 446 L176 446 C380 420 440 200 456 0 Z" fill="var(--brand-orange)"/>
      <path d="M463 0 L780 0 L780 446 L183 446 C387 420 447 200 463 0 Z" fill="var(--card-white)"/>
      <path d="M470 0 L780 0 L780 446 L190 446 C394 420 454 200 470 0 Z" fill="var(--brand-blue)"/>
    </svg>
    <div class="brand">
      <span class="brand__dot"></span>
      <span class="brand__name">BRIGHT LANTERN<br>COLLECTIVE</span>
    </div>
  </section>

  <section class="card card--back" aria-label="Card back">
    <svg class="card__art" viewBox="0 0 780 446" preserveAspectRatio="none" aria-hidden="true">
      <rect width="780" height="446" fill="var(--brand-blue)"/>
      <path d="M364 0 C304 150 324 330 544 446 L780 446 L780 0 Z" fill="var(--card-white)"/>
      <path d="M368 0 C308 150 328 330 548 446 L780 446 L780 0 Z" fill="var(--brand-orange)"/>
      <path d="M380 0 C320 150 340 330 560 446 L780 446 L780 0 Z" fill="var(--card-white)"/>
    </svg>

    <div class="person">
      <p class="person__name">MATHÉO VRANEL</p>
      <p class="person__role">Founder &amp; CEO</p>
    </div>

    <ul class="contacts">
      <li class="contacts__item">
        <svg class="contacts__icon" viewBox="0 0 24 24" aria-hidden="true"><circle cx="12" cy="12" r="11" fill="var(--brand-orange)"/><path d="M8 6.5c.6-.4 1.3-.3 1.6.3l1 1.8c.3.5.1 1.1-.3 1.4l-.7.5c.6 1.4 1.6 2.4 3 3l.5-.7c.3-.4.9-.6 1.4-.3l1.8 1c.6.3.7 1 .3 1.6l-.6.8c-.5.6-1.3.8-2 .6-3.1-1-5.4-3.3-6.4-6.4-.2-.7 0-1.5.6-2z" fill="var(--card-white)"/></svg>
        <span>+590 690 482 517</span>
      </li>
      <li class="contacts__item">
        <svg class="contacts__icon" viewBox="0 0 24 24" aria-hidden="true"><rect x="2" y="5" width="20" height="14" rx="2" fill="var(--brand-orange)"/><path d="M3 6.5l9 6.5 9-6.5" fill="none" stroke="var(--card-white)" stroke-width="1.8"/></svg>
        <span>ceo@brightlanterncollective.com</span>
      </li>
      <li class="contacts__item">
        <svg class="contacts__icon" viewBox="0 0 24 24" aria-hidden="true"><circle cx="12" cy="12" r="10" fill="var(--brand-orange)"/><path d="M2 12h20M12 2c3 3 3 17 0 20M12 2c-3 3-3 17 0 20" fill="none" stroke="var(--card-white)" stroke-width="1.4"/></svg>
        <span>www.brightlanterncollective.com</span>
      </li>
      <li class="contacts__item">
        <span class="contacts__social"><span></span><span></span></span>
        <span>@brightlanterncollective</span>
      </li>
    </ul>

    <div class="brand">
      <span class="brand__dot"></span>
      <span class="brand__name">BRIGHT LANTERN<br>COLLECTIVE</span>
    </div>
  </section>

</body>
</html>
```